Graphic Design Project

We have a project that needs a tidy up. Its already designed, however what we are wanting is somebody to tidy up the secondary pages with some cool design elements, as buttons to eliminate the need to too much elements.

I can enclose all the pages as references plus the mind map so that you understand the project. There is no coding needed, just the reshaped page layout and buttons where certain images are.

Each elelement is spelt out so it should not be too hard. I will also upload where the advertising goes as well as a reference.

The aim with these pages is to funnel down the customer so that they can go to the database on the minimum amount of clicks.
Updates

with the design elements, all we are looking for is someone to take all the page layouts that I have submitted, and put them back in order, so that in the second tier website it funnels down to a database development.

Whoever gets back to me, I will upload the mindmap and also the advertising schedule that will be built into the page.

The majority of pages we want to keep them the same, and the reference pages that i SENT THROUGH ARE JUST GUIDES.

If there are any questions please come back ASAP, as we are wanting to get this application finished ASAP.

can all designers please submit designs or come back ASAP as we need to get this project finalized. If there are some concerns what to do please ask..

We are running out of time guys, as we need to get this finalized.

am including the link to the site as it is now. The front page is the way it should be, so thats constant.

The secondary pages, which I have asked for the submitted designs of will have advertising in the top and bottom banner as well as two tiles down the RHS.

We want the design to draw the customer into the database development, so that its simple and clean looking, and we can eliminate too many clicks.

www.bravotrellis.com.au/site

any questions come back to me asap.

Hi there, we are approaching the deadline and no designers have sent through the pages that we require. Its not a complicated project as the design is already laid out for the home page, and if we can the second level pages (the ones that you are working on), can almost be similar.

At this stage, the first one we get designs back from, we will go with, especially as the client is wanting to show potential investors the layout....

if in doubt over the weekend, please email me. domvarnish@quorlmail.com
or  skype at:

dom.varnish

Reason: due to designers not submitting any designs or coming back with any feedback conclusively we are extending the deadline a few more days.

Target Market(s)

35 to 50 age bracket business owners

Industry/Entity Type

Advertising

Requirements
Must have
• must use existing colours of the brand, be attractive and compliment what is already in place.
Nice to have
• features are focus on functionality
Should not have
• over cluttered.

```html
<!DOCTYPE html>
<html lang="en">
<head>
<meta charset="utf-8">
<title>Bravotrellis – Group and Calendar of Events</title>
<link href="https://fonts.googleapis.com/css2?family=Roboto:wght@400;500;700&display=swap" rel="stylesheet">
<style>
:root{
  --brand:#0a8fd6;
  --brand-dark:#0a2f52;
  --nav-top:#1d4b78;
  --text:#222;
  --muted:#444;
  --rule:#cfcfcf;
  --tile:#b1b9bd;
  --arrow:#7aaac4;
  --bg:#fff;
}
*{box-sizing:border-box;margin:0;padding:0}
html,body{width:1040px;height:1200px;overflow:hidden;background:var(--bg);font-family:"Roboto",Arial,sans-serif;color:var(--text)}
.page{position:relative;width:1040px;height:1200px}
.topbar{position:absolute;top:0;left:0;right:0;height:25px;background:linear-gradient(#2aa6e6,#0a8fd6)}
.login{position:absolute;right:132px;top:6px;color:#fff;font-size:11px;display:flex;align-items:center;gap:10px}
.header-glow{position:absolute;top:25px;left:0;right:0;height:30px;background:linear-gradient(#dff0fb,#fff)}
.brand{position:absolute;left:145px;top:48px;display:flex;align-items:center;gap:8px}
.brand-mark{width:18px;height:18px;background:var(--brand)}
.brand-name{font-size:30px;font-weight:700;color:var(--brand)}
.brand-tag{position:absolute;left:145px;top:86px;font-size:8px;color:var(--muted)}
.ad-banner{position:absolute;left:385px;top:44px;width:374px;height:49px;border:2px solid #e02424;display:flex}
.ad-banner .ad-left{width:125px;display:flex;align-items:center;justify-content:center;font-size:11px;font-weight:700;color:var(--brand-dark);background:#fff}
.ad-banner .ad-right{flex:1;background:linear-gradient(90deg,#3f7a35,#2c5d28);color:#fff;font-size:11px;font-weight:700;font-style:italic;padding:9px 14px;line-height:15px}
.follow{position:absolute;left:855px;top:47px;font-size:11.5px;color:var(--brand)}
.socials{position:absolute;left:781px;top:75px;display:flex;gap:5px}
.socials span{width:17px;height:17px;display:block}
.nav{position:absolute;top:132px;left:0;right:0;height:25px;background:linear-gradient(var(--nav-top),var(--brand-dark))}
.nav ul{list-style:none;display:flex;position:absolute;left:119px;top:0;height:25px}
.nav li{color:#fff;font-size:11px;line-height:25px;padding:0 26px;border-right:1px solid #3c6590}
.nav li:last-child{border-right:0}
.main{position:absolute;left:146px;top:175px;width:460px}
h2{font-weight:400;color:var(--brand);font-size:17.5px;margin-bottom:8px}
.main p{font-size:9.8px;line-height:17.6px;color:var(--text)}
.media{position:absolute}
.select{position:absolute;width:175px;height:21px;border:1px solid #999;font-size:11px;padding:3px 6px;color:#333;background:#fff}
.select::after{content:"";position:absolute;right:3px;top:3px;width:13px;height:13px;border:1px solid #888;background:linear-gradient(#fff,#ddd)}
.select i{position:absolute;right:7px;top:8px;width:0;height:0;border-left:3px solid transparent;border-right:3px solid transparent;border-top:4px solid #000;z-index:1}
.side{position:absolute;left:680px;width:222px}
.side h3{font-weight:400;color:var(--brand);font-size:17.5px;display:flex;align-items:center;gap:10px}
.side .date{font-size:10.5px;font-weight:500;margin:12px 0 8px}
.side p{font-size:9.8px;line-height:17.6px;color:var(--muted)}
.side a{display:block;font-size:10.5px;font-weight:700;color:var(--brand);text-decoration:none;margin:6px 0 12px}
.side hr{border:0;border-top:1px dotted var(--rule);margin-top:4px}
.tile{position:absolute;left:718px;width:144px;height:120px;background:var(--tile);color:#fff;font-size:21px;display:flex;align-items:center;justify-content:center}
</style>
</head>
<body>
<div class="page">
  <div class="topbar">
    <div class="login">
      <svg width="12" height="14" viewBox="0 0 12 14"><circle cx="6" cy="4" r="3" fill="#cfe9f8"/><path d="M0 14c0-5 12-5 12 0z" fill="#cfe9f8"/></svg>
      UNIQUE LOGIN
    </div>
  </div>
  <div class="header-glow"></div>

  <div class="brand"><span class="brand-mark"></span><span class="brand-name">Bravotrellis</span></div>
  <div class="brand-tag">The trusted place for racehorse syndication</div>

  <div class="ad-banner">
    <div class="ad-left">Corner Grocer</div>
    <div class="ad-right">The future of independent<br>retailing across Australia.</div>
  </div>

  <div class="follow">Follow Us</div>
  <div class="socials">
    <span style="background:#3b5b9a"></span>
    <span style="background:#3fb6e8"></span>
    <span style="background:#f4811f"></span>
    <span style="background:#1a72ad"></span>
    <span style="background:#c8232c"></span>
    <span style="background:#333"></span>
  </div>

  <nav class="nav">
    <ul>
      <li>Home</li><li>About Us</li><li>Syndicate Information</li><li>Shares Available</li><li>Owners Corner</li><li>Membership</li><li>Useful Tools</li>
    </ul>
  </nav>

  <section class="main" style="top:175px">
    <h2>Group and Calendar of events for Australia</h2>
    <p>Nemo enim ipsam voluptatem quia voluptas sit aspernatur aut odit aut fugit, sed quia consequuntur magni dolores eos qui ratione voluptatem sequi nesciunt. Neque porro quisquam est, qui dolorem ipsum quia dolor sit amet, consectetur, adipisci velit, sed quia non numquam eius modi tempora incidunt ut labore et dolore magnam aliquam quaerat voluptatem.</p>
  </section>
  <div class="media" role="img" aria-label="Coloured map of Australia divided into states and territories" style="left:172px;top:288px;width:216px;height:196px;background:linear-gradient(135deg,#f6a05e 0%,#f2ec3c 40%,#8fbde3 70%,#f07b5c 100%);border-radius:40% 45% 35% 30%"></div>
  <div class="select" style="left:414px;top:353px">Western Australia<i></i></div>

  <section class="main" style="top:519px">
    <h2>Recent Winners &amp; Replays</h2>
    <p>Nemo enim ipsam voluptatem quia voluptas sit aspernatur aut odit aut fugit, sed quia consequuntur magni dolores eos qui ratione voluptatem sequi nesciunt. Neque porro quisquam est, qui dolorem ipsum quia dolor sit amet, consectetur, adipisci velit, sed quia non numquam eius modi tempora incidunt ut labore et dolore magnam aliquam quaerat voluptatem.</p>
  </section>
  <div class="media" role="img" aria-label="Jockey riding a chestnut racehorse at full gallop" style="left:143px;top:634px;width:249px;height:135px;background:linear-gradient(120deg,#6f8c3f,#8a4a2a 50%,#3b3f8a)"></div>
  <div class="select" style="left:414px;top:675px">Recent winners<i></i></div>

  <section class="main" style="top:799px">
    <h2>Database of owners</h2>
    <p>Nemo enim ipsam voluptatem quia voluptas sit aspernatur aut odit aut fugit, sed quia consequuntur magni dolores eos qui ratione voluptatem sequi nesciunt.</p>
  </section>
  <div class="media" role="img" aria-label="Owners celebrating with their winning horse at the racecourse" style="left:143px;top:874px;width:249px;height:136px;background:linear-gradient(180deg,#7aa0c8,#4c6a3a 55%,#5b8a3a)"></div>
  <div class="select" style="left:414px;top:915px">Database<i></i></div>

  <aside class="side" style="top:174px">
    <h3><svg width="15" height="13" viewBox="0 0 15 13"><rect x=".5" y=".5" width="14" height="12" fill="#fff" stroke="#4a74b8"/><rect x="2" y="3" width="5" height="5" fill="#4a74b8"/><path d="M8 3h5M8 5h5M8 7h5M2 10h11" stroke="#4a74b8"/></svg>Industry news</h3>
    <div class="date">Jul 16, 2012</div>
    <p>Nemo enim ipsam voluptatem quia voluptas sit aspernatur aut odit aut fugit, sed quia consequ-</p>
    <a>Read more</a>
    <div class="date">Jul 16, 2012</div>
    <p>Nemo enim ipsam voluptatem quia voluptas sit aspernatur aut odit aut fugit, sed quia conse-</p>
    <a>Read more</a>
    <hr>
  </aside>

  <aside class="side" style="top:394px">
    <h3><svg width="12" height="13" viewBox="0 0 12 13"><rect y="0" width="12" height="3" fill="var(--brand)"/><rect y="5" width="12" height="3" fill="var(--brand)"/><rect y="10" width="12" height="3" fill="var(--brand)"/></svg>Database of Owners</h3>
    <div class="date" style="font-size:11.5px">Owner</div>
    <p>Nemo enim ipsam voluptatem quia voluptas sit aspernatur aut odit aut fugit, sed quia consequuntur magni dolores eos qui ratione voluptatem sequi.</p>
    <a>View Database</a>
    <hr>
  </aside>

  <aside class="side" style="top:577px">
    <h3><svg width="12" height="12" viewBox="0 0 12 12"><rect width="12" height="12" rx="2" fill="#f57d00"/><rect x="3" y="3" width="6" height="6" rx="1" fill="#fff"/></svg>Blog</h3>
    <div class="date" style="font-size:11.5px">20 October 2012</div>
    <div style="display:flex;gap:10px">
      <svg width="44" height="48" viewBox="0 0 44 48"><path d="M2 2h24l8 8v34H2z" fill="#f4f4f4" stroke="#999"/><path d="M7 14h20M7 19h20M7 24h20M7 29h14" stroke="#bbb"/><path d="M18 44l18-22 4 3-18 22-6 2z" fill="#333"/></svg>
      <div><p>Nemo enim ipsam voluptatem quia voluptas sit aspernatur aut odit aut fugit, sed quia consequuntur</p><a>View Blog</a></div>
    </div>
    <hr style="margin-top:-4px">
  </aside>

  <aside class="side" style="top:736px">
    <h3><svg width="12" height="10" viewBox="0 0 12 10"><rect y="1" width="12" height="2" fill="var(--brand)"/><rect y="7" width="12" height="2" fill="var(--brand)"/></svg>Syndicate Match</h3>
    <p style="margin-top:10px">Nemo enim ipsam voluptatem quia voluptas sit aspernatur aut odit aut fugit, sed quia consequuntur magni dolores eos qui ratione voluptatem sequi.</p>
    <hr style="margin-top:14px">
  </aside>

  <svg style="position:absolute;left:776px;top:862px" width="30" height="22" viewBox="0 0 30 22"><path d="M15 0L30 15H22V22H8V15H0z" fill="var(--arrow)"/></svg>
  <div class="tile" style="top:889px">180x150</div>
  <div class="tile" style="top:1017px">180x150</div>
  <svg style="position:absolute;left:776px;top:1141px" width="30" height="22" viewBox="0 0 30 22"><path d="M15 22L30 7H22V0H8V7H0z" fill="var(--arrow)"/></svg>
</div>
</body>
</html>
```